Medical Practice Business Card

we need a business card for our new medical ophthalmology practice based in Needham Massachusetts. we are looking for a simple , modern and elegant design.
the card needs to contain the following
1- the logo of our practice (please see attached file)
2- the name of the practice : "Harbor Crest Vision Care"
3- Doctor's Name: Tobias Werrin MD PhD
4- Specialty: Board-Certified Vitreoretinal Surgeon
5- practice address: 382 Palden Ave, Suite 210, Elmswick AV 04491
7- Office number: 617- 418 - 2297
8- fax number: 617- 729 - 3186
9- email: info@hcvisioncare.com
10- website: www.hcvisioncare.com
see description

```html
<!DOCTYPE html>
<html lang="en">
<head>
<meta charset="utf-8">
<title>Harbor Crest Vision Care – Business Card</title>
<link href="https://fonts.googleapis.com/css2?family=Poppins:wght@300;400;700&display=swap" rel="stylesheet">
<style>
  :root {
    --stage: #2b2f36;
    --paper: #ffffff;
    --navy: #0e2d5a;
    --ink: #1b1d22;
    --muted: #5d6168;
    --sky: #6cc7dc;
    --ocean: #2f6791;
    --deep: #0b3566;
  }
  * { margin: 0; padding: 0; box-sizing: border-box; }
  html, body { width: 1200px; height: 780px; overflow: hidden; }
  body {
    background: var(--stage);
    font-family: "Poppins", sans-serif;
    display: flex;
    align-items: center;
    justify-content: center;
    gap: 60px;
  }
  .card {
    width: 520px;
    height: 300px;
    border-radius: 18px;
    position: relative;
    overflow: hidden;
    box-shadow: 0 14px 30px rgba(0,0,0,.35);
  }
  .card-front { background: var(--paper); color: var(--ink); }
  .card-back {
    background: linear-gradient(200deg, var(--sky) 0%, var(--ocean) 38%, var(--deep) 75%);
    display: flex; align-items: center; justify-content: center;
  }
  .brand { display: flex; align-items: center; gap: 12px; }
  .brand-dot { width: 14px; height: 14px; border-radius: 50%; flex: none; }
  .brand-name { font-weight: 700; letter-spacing: .04em; text-transform: uppercase; line-height: 1.05; }
  .card-front .brand { position: absolute; left: 96px; top: 34px; }
  .card-front .brand-dot { background: var(--navy); }
  .card-front .brand-name { color: var(--navy); font-size: 25px; }
  .card-back .brand-dot { background: #ffffff; width: 18px; height: 18px; }
  .card-back .brand-name { color: #ffffff; font-size: 32px; }
  .doctor { position: absolute; left: 96px; top: 110px; }
  .doctor-name { font-size: 21px; color: var(--navy); letter-spacing: .02em; }
  .doctor-name .first { font-weight: 700; }
  .doctor-name .last { font-weight: 300; }
  .doctor-name .degree { font-size: 9px; font-weight: 400; margin-left: 4px; }
  .doctor-title { font-size: 11px; font-weight: 300; color: var(--muted); margin-top: 2px; }
  .address {
    position: absolute; left: 40px; top: 190px; width: 190px;
    font-size: 13px; line-height: 1.45; color: var(--ink);
  }
  .divider { position: absolute; left: 238px; top: 180px; width: 1px; height: 90px; background: var(--ink); }
  .contacts { position: absolute; left: 256px; top: 172px; list-style: none; }
  .contacts li { display: flex; align-items: center; gap: 10px; font-size: 14px; height: 25px; }
  .contacts svg { width: 15px; height: 15px; fill: var(--navy); flex: none; }
</style>
</head>
<body>
  <section class="card card-front">
    <div class="brand">
      <span class="brand-dot"></span>
      <span class="brand-name">Harbor Crest<br>Vision Care</span>
    </div>
    <div class="doctor">
      <p class="doctor-name"><span class="first">TOBIAS</span> <span class="last">WERRIN</span><span class="degree">MD PhD</span></p>
      <p class="doctor-title">Certified Vitreoretinal Surgeon</p>
    </div>
    <p class="address">382 Palden Ave, Suite 210,<br>Elmswick AV 04491</p>
    <span class="divider"></span>
    <ul class="contacts">
      <li><svg viewBox="0 0 24 24"><path d="M6.6 10.8a15 15 0 0 0 6.6 6.6l2.2-2.2c.3-.3.7-.4 1-.2 1.1.4 2.3.6 3.6.6.6 0 1 .4 1 1V20c0 .6-.4 1-1 1A17 17 0 0 1 3 4c0-.6.4-1 1-1h3.5c.6 0 1 .4 1 1 0 1.3.2 2.5.6 3.6.1.3 0 .7-.2 1z"/></svg>617- 418 - 2297</li>
      <li><svg viewBox="0 0 24 24"><path d="M6 2h9l3 3v4h2a2 2 0 0 1 2 2v9a2 2 0 0 1-2 2H4a2 2 0 0 1-2-2v-9a2 2 0 0 1 2-2h2zm2 2v5h8V6h-2V4zm0 9v2h2v-2zm4 0v2h2v-2zm4 0v2h2v-2zm-8 4v2h2v-2zm4 0v2h2v-2zm4 0v2h2v-2z"/></svg>617- 729 - 3186</li>
      <li><svg viewBox="0 0 24 24"><path d="M2 5h20v14H2zm2 2v.5l8 5.5 8-5.5V7z"/></svg>info@hcvisioncare.com</li>
      <li><svg viewBox="0 0 24 24"><path d="M12 2a10 10 0 1 0 0 20 10 10 0 0 0 0-20zm6.9 9h-3a15 15 0 0 0-1.3-6A8 8 0 0 1 18.9 11zM12 4.1c.9 1.3 1.7 3.8 1.9 6.9h-3.8c.2-3.1 1-5.6 1.9-6.9zM9.4 5a15 15 0 0 0-1.3 6h-3A8 8 0 0 1 9.4 5zM5.1 13h3a15 15 0 0 0 1.3 6A8 8 0 0 1 5.1 13zm6.9 6.9c-.9-1.3-1.7-3.8-1.9-6.9h3.8c-.2 3.1-1 5.6-1.9 6.9zm2.6-.9a15 15 0 0 0 1.3-6h3a8 8 0 0 1-4.3 6z"/></svg>www.hcvisioncare.com</li>
    </ul>
  </section>

  <section class="card card-back">
    <div class="brand">
      <span class="brand-dot"></span>
      <span class="brand-name">Harbor Crest<br>Vision Care</span>
    </div>
  </section>
</body>
</html>
```